Web Site for Strategy and Technology Consulting Company

We are looking for a website design that engages potential customers to understand our services and contact us. In this contest, we are looking for a homepage design, but the winning designer will be favored for the design of some of the more complicated interior pages of the site. An additional contest (or contests) for these pages will be added soon.

PLATROM AND RESPONSIVE DESIGN
The site will be implemented in WordPress using the Elementor page builder.
We are looking for a design that will look good on phones are well as laptop browsers.

UPLOADED FILES INCLUDE:
1a A wireframe of the homepage we are looking for. The Uploaded PDF also includes a draft of the text proposed for the homepage. Designers are free to go beyond the wireframe, but all elements of the wireframe should be included.
1b A Word document with the draft text of the homepage.
2a-d The Norvalith logo. Two versions are included – a dark version which works well against a light background, and a light version which works well against a dark background.
3 The Norvalith color palette with HEX and RGB values. Designers are not limited to this palette, but colors should be complementary.
4 A draft of the homepage menu
5 Service sheets with information on the services we provide

MORE ABOUT NORVALITH
Norvalith is a consulting company focused on transforming businesses through software. Our tagline, “Transformation Delivered,” recognizes the gap business often have between business transformation and the software they end up with. By listening to our customers and understanding their vision and where they are, we help get our customers where they want to go.

We increase our capability by working with many consultants and partners, allowing us to provide our customers with the best people and the software that best suits them.

Industry/Entity Type

Consulting

Number of Pages Required

1 page

Font styles to use
Sans Serif

Requirements
Must have
• the content represented on the wireframe uploaded
Nice to have
• interactive features, such as roll-over icons that reveal additional information

```html
<!DOCTYPE html>
<html lang="en">
<head>
<meta charset="utf-8">
<title>Norvalith — Transformation Delivered</title>
<link rel="stylesheet" href="https://fonts.googleapis.com/css2?family=Lexend:wght@300;400;500;600;700&display=swap">
<style>
:root{
  --ink:#141414;
  --body:#3a3a3a;
  --blue:#2b62a3;
  --blue-dark:#1f4f8c;
  --sky:#e2edf8;
  --yellow:#f0c21a;
  --yellow-deep:#dcb21c;
  --night:#141414;
  --muted:#8a8f98;
  --white:#ffffff;
}
*{box-sizing:border-box;margin:0;padding:0}
html,body{width:1200px;height:5076px;overflow:hidden;background:var(--white)}
body{font-family:"Lexend",sans-serif;color:var(--ink);position:relative}
.page{position:relative;width:1200px;height:5076px;overflow:hidden}
.abs{position:absolute}
.backdrop{position:absolute;left:0;top:0;width:1200px;height:5076px}

/* header */
.site-header{position:absolute;left:0;top:0;width:1200px;height:85px;border-bottom:1px solid #ececec;background:var(--white);z-index:3}
.brand{position:absolute;display:flex;align-items:center;gap:10px;font-weight:500;letter-spacing:-.5px}
.brand-mark{width:12px;height:12px;border-radius:50%;background:var(--blue)}
.site-header .brand{left:197px;top:20px;font-size:38px;color:#4a4a4a}
.nav{position:absolute;left:465px;top:34px;display:flex;gap:0;font-size:11px;color:var(--ink)}
.nav-item{position:relative;padding:0 22px;}
.nav-item:first-child{font-weight:600}
.nav-item+.nav-item::before{content:"";position:absolute;left:-2px;top:5px;width:4px;height:4px;border-radius:50%;background:var(--yellow)}
.nav-item.has-sub::after{content:"";position:absolute;left:50%;top:24px;width:4px;height:4px;border-right:1px solid #555;border-bottom:1px solid #555;transform:translateX(-50%) rotate(45deg)}
.btn{position:absolute;display:flex;align-items:center;justify-content:center;border-radius:20px;font-size:9px;font-weight:600;letter-spacing:2px;text-transform:uppercase}
.btn-contact{left:890px;top:28px;width:112px;height:32px;background:var(--yellow);color:var(--white)}

/* hero */
.hero-photo{position:absolute;left:0;top:85px;width:760px;height:720px;background:linear-gradient(135deg,#3c4656 0%,#8a7a6d 30%,#c9b8a6 55%,#e9edf3 80%);-webkit-mask-image:linear-gradient(90deg,#000 40%,transparent 95%);mask-image:linear-gradient(90deg,#000 40%,transparent 95%)}
.pixel-field{position:absolute;border-radius:20px;filter:blur(2px)}
.hero-copy{position:absolute;left:538px;top:148px;border-left:3px solid var(--yellow);padding-left:26px;height:180px}
.eyebrow{font-size:10px;font-weight:600;letter-spacing:4px;text-transform:uppercase;color:var(--blue)}
.hero-title{font-size:50px;font-weight:400;line-height:1;margin-top:20px;color:var(--ink);letter-spacing:-.5px}
.btn-start{position:relative;margin-top:22px;width:146px;height:28px;background:var(--blue);color:var(--white);font-size:8px}

/* intro */
.intro{position:absolute;left:197px;top:926px;width:440px}
.intro-head{border-left:3px solid var(--yellow);padding-left:22px}
.intro-title{font-size:40px;font-weight:400;line-height:1;margin-top:12px;letter-spacing:-.3px}
.small{font-size:9.5px;line-height:1.75;color:var(--body)}
.intro .small{margin-top:30px}
.bullets{list-style:none;margin-top:12px}
.bullets li{position:relative;padding-left:18px;font-size:9.5px;line-height:1.75;color:var(--body)}
.bullets li::before{content:"";position:absolute;left:0;top:6px;width:4px;height:4px;border-radius:50%;background:var(--yellow)}
.intro-close{margin-top:20px}
.tilt-photo{position:absolute;border-radius:14px}
.scroll-cue{position:absolute;left:24px;top:1015px;width:12px;height:20px;border:1.5px solid var(--blue);border-radius:7px}
.scroll-cue::after{content:"";position:absolute;left:4px;top:4px;width:2px;height:5px;background:var(--blue);border-radius:1px}

/* services */
.centered{position:absolute;left:0;width:1200px;text-align:center}
.section-title{font-size:50px;font-weight:400;line-height:1;letter-spacing:-.5px}
.title-rule{display:block;width:54px;height:3px;background:var(--yellow);margin:8px auto 0}
.service-card{position:absolute;width:254px;height:184px;border-radius:6px;background:linear-gradient(135deg,var(--yellow-deep),#ecc43a);color:var(--white);text-align:center;padding-top:34px}
.service-icon{display:block;margin:0 auto}
.service-name{font-size:11px;font-weight:600;margin-top:18px}
.service-text{font-size:9px;line-height:1.5;margin:14px auto 0;width:150px;color:#fff6d6}
.caption{font-size:12px;color:var(--body)}

/* people */
.avatar{position:absolute;border-radius:50%;background:radial-gradient(circle at 50% 40%,#d9b59a,#8f6a55 70%,#5d4a3f)}
.avatar.ring{box-shadow:0 0 0 4px var(--white),0 0 0 7px var(--yellow)}
.avatar.soft{filter:blur(3px);opacity:.8}
.people-copy{font-size:10.5px;line-height:2;color:var(--ink)}

/* testimonials */
.quote-mark{position:absolute;left:374px;top:3270px}
.reviews{position:absolute;left:197px;top:3440px;width:360px;color:var(--white)}
.reviews .eyebrow{color:var(--white)}
.reviews-title{font-size:52px;font-weight:400;line-height:1;margin-top:10px}
.reviews-title::after{content:"";display:block;width:315px;height:3px;background:var(--yellow);margin-top:4px}
.reviews .small{color:#dbe6f4;margin-top:20px;font-size:10px;line-height:2.2}
.btn-view{position:relative;margin-top:28px;width:126px;height:32px;background:var(--yellow);color:var(--white);font-size:8px}
.review-card{position:absolute;width:313px;height:193px;background:var(--white);border-radius:6px;padding:28px 30px}
.review-head{display:flex;align-items:center;gap:14px}
.review-face{width:44px;height:44px;border-radius:50%;background:radial-gradient(circle at 50% 40%,#c9a58c,#6a5446 75%)}
.review-name{font-size:8px;font-weight:600;letter-spacing:.5px}
.stars{color:var(--yellow);font-size:9px;letter-spacing:1px;margin-top:4px}
.review-quote{position:absolute;right:34px;top:30px}
.review-card .small{font-size:10px;line-height:1.7;color:#222;margin-top:18px}
.dot{position:absolute;width:8px;height:8px;border-radius:50%;background:var(--white)}

/* technologies */
.tech-card{position:absolute;top:4064px;width:254px}
.tech-photo{width:254px;height:300px;border-radius:8px}
.tech-label{text-align:center;font-size:14px;font-weight:600;margin-top:38px}
.carousel-arrow{position:absolute;top:4182px;width:60px;height:60px;border-radius:50%;background:#e7eff8}

/* footer */
.footer-brand{left:197px;top:4742px;font-size:40px;color:var(--white)}
.footer-brand .brand-mark{background:var(--blue)}
.footer-about{position:absolute;left:197px;top:4812px;width:270px;font-size:10px;line-height:2.2;color:#d8d8d8}
.copyright{position:absolute;left:197px;top:4928px;font-size:9px;color:#d8d8d8}
.socials{position:absolute;left:195px;top:4966px;display:flex;gap:14px}
.socials span{width:20px;height:20px;border-radius:50%;background:var(--yellow)}
.footer-col{position:absolute;top:4746px;color:var(--white)}
.footer-col h4{font-size:13px;font-weight:600}
.footer-col ul{list-style:none;margin-top:14px}
.footer-col li{font-size:10px;color:#d8d8d8;height:36.5px}
.contact-row{display:flex;align-items:center;gap:16px;height:57px;font-size:9.5px;color:#d8d8d8;line-height:1.6}
.contact-icon{flex:none;width:36px;height:36px;border-radius:50%;border:1px solid #555;display:flex;align-items:center;justify-content:center}
</style>
</head>
<body>
<div class="page">

  <div class="hero-photo" role="img" aria-label="Photo of business colleagues reviewing work on a laptop"></div>

  <svg class="backdrop" viewBox="0 0 1200 5076" aria-hidden="true">
    <!-- hero cut -->
    <polygon points="0,905 560,712 620,760 1200,608 1200,930 0,930" fill="#fff"/>
    <polyline points="69,896 560,700 620,750 1200,600" fill="none" stroke="#2b62a3" stroke-width="1.5"/>
    <line x1="30" y1="780" x2="30" y2="1000" stroke="#2b62a3" stroke-width="1" stroke-dasharray="2 3"/>
    <!-- services band -->
    <polygon points="0,1598 561,1378 630,1478 1200,1300 1200,2236 630,2418 561,2312 0,2520" fill="#e2edf8"/>
    <polyline points="0,1566 561,1349 630,1448 1137,1270" fill="none" stroke="#2b62a3" stroke-width="1.5"/>
    <circle cx="1137" cy="1270" r="4" fill="#2b62a3"/>
    <polyline points="0,2542 561,2330 630,2436 1200,2252" fill="none" stroke="#b8cfe6" stroke-width="1.5"/>
    <!-- testimonials band -->
    <polygon points="0,3160 571,3250 650,3160 1200,2900 1200,3700 650,3870 571,3790 0,3960" fill="#2b62a3"/>
    <line x1="0" y1="3215" x2="1137" y2="2896" stroke="#f0c21a" stroke-width="1.5"/>
    <circle cx="1137" cy="2896" r="4" fill="#f0c21a"/>
    <line x1="0" y1="3975" x2="1103" y2="3645" stroke="#f0c21a" stroke-width="1.5"/>
    <circle cx="1103" cy="3645" r="4" fill="#f0c21a"/>
    <!-- footer -->
    <polygon points="0,4722 1200,4430 1200,5076 0,5076" fill="#141414"/>
    <line x1="0" y1="4692" x2="1137" y2="4409" stroke="#2b62a3" stroke-width="1.5"/>
    <circle cx="1137" cy="4409" r="4" fill="#2b62a3"/>
  </svg>

  <header class="site-header">
    <div class="brand"><span class="brand-mark"></span>Norvalith</div>
    <nav class="nav">
      <span class="nav-item">Home</span>
      <span class="nav-item has-sub">About Us</span>
      <span class="nav-item has-sub">Services</span>
      <span class="nav-item has-sub">Insights</span>
      <span class="nav-item has-sub">Join Us</span>
    </nav>
    <span class="btn btn-contact">Contact</span>
  </header>

  <!-- hero -->
  <div class="pixel-field" style="left:670px;top:270px;width:520px;height:320px;background:radial-gradient(ellipse at 60% 50%,rgba(240,194,26,.35),rgba(43,98,163,.25) 50%,transparent 75%)" role="img" aria-label="Scattered yellow and blue pixel squares"></div>
  <section class="hero-copy">
    <p class="eyebrow">Norvalith provides</p>
    <h1 class="hero-title">Transformation<br>Delivered</h1>
    <span class="btn btn-start">Get Started</span>
  </section>

  <!-- intro -->
  <span class="scroll-cue"></span>
  <section class="intro">
    <div class="intro-head">
      <p class="eyebrow">Transforming</p>
      <h2 class="intro-title">Businesses<br>Through Software</h2>
    </div>
    <p class="small">We do more for our customers than implement software. We listen. We work to understand where they are in their transformation journey and where they want to go. We partner with them to clear the roadblocks that stand in their way, ensuring they reach their destination. At Norvalith, we:</p>
    <ul class="bullets">
      <li>Focus on business value, with an emphasis on delivering value quickly.</li>
      <li>Meet our customers where they are without locking them up to the beginning of their journey.</li>
      <li>Provide a wide range of services, from strategy to product support.</li>
      <li>Commit to our customer’s long-term success.</li>
    </ul>
    <p class="small intro-close">Norvalith is business transformation, delivered.</p>
  </section>
  <div class="tilt-photo" style="left:658px;top:902px;width:205px;height:365px;background:linear-gradient(160deg,#f3c98a,#a8805e 50%,#5b4a40)" role="img" aria-label="Hands on a laptop with floating document icons"></div>
  <div class="tilt-photo" style="left:871px;top:823px;width:207px;height:365px;background:linear-gradient(160deg,#e7a45a,#b88d6a 45%,#7b8fa6)" role="img" aria-label="Person typing on a laptop with a checklist overlay"></div>

  <div class="pixel-field" style="left:900px;top:1310px;width:300px;height:200px;background:radial-gradient(ellipse at 60% 50%,rgba(43,98,163,.35),rgba(240,194,26,.2) 55%,transparent 75%)" role="img" aria-label="Scattered blue and yellow pixel squares"></div>

  <!-- services -->
  <section class="centered" style="top:1550px">
    <p class="eyebrow">Transformation</p>
    <h2 class="section-title" style="margin-top:12px">Supported By<br>Technology</h2>
    <span class="title-rule" style="margin-top:-4px"></span>
    <p class="small" style="width:740px;margin:30px auto 0;font-size:9.5px;line-height:2">During our early years, Norvalith focused only on business transformation. We came to realize that successful transformation often depended on quality software implementations, and often more than one. Now we focus on five things, the five things most businesses need to reach their goals.</p>
  </section>

  <div class="service-card" style="left:197px;top:1783px">
    <svg class="service-icon" width="40" height="40" viewBox="0 0 40 40"><rect x="6" y="10" width="18" height="24" rx="2" fill="#2b62a3"/><rect x="10" y="15" width="4" height="4" fill="#fff"/><rect x="16" y="15" width="4" height="4" fill="#fff"/><rect x="10" y="22" width="4" height="4" fill="#fff"/><circle cx="30" cy="12" r="6" fill="#f7dc74"/></svg>
    <p class="service-name">Business Transformation</p>
    <p class="service-text">Define and execute your strategy</p>
  </div>
  <div class="service-card" style="left:471px;top:1783px">
    <svg class="service-icon" width="40" height="40" viewBox="0 0 40 40"><circle cx="20" cy="20" r="13" fill="none" stroke="#2b62a3" stroke-width="4" stroke-dasharray="6 3"/><circle cx="20" cy="20" r="6" fill="#2b62a3"/><circle cx="29" cy="10" r="5" fill="#f7dc74"/></svg>
    <p class="service-name">ERP Implementations</p>
    <p class="service-text">Assess, upgrade, and implement ERP solutions to meet your needs</p>
  </div>
  <div class="service-card" style="left:747px;top:1783px">
    <svg class="service-icon" width="40" height="40" viewBox="0 0 40 40"><rect x="6" y="6" width="22" height="26" rx="2" fill="#2b62a3"/><rect x="10" y="11" width="14" height="3" fill="#fff"/><rect x="10" y="17" width="10" height="3" fill="#fff"/><circle cx="28" cy="28" r="6" fill="#f7dc74" stroke="#2b62a3" stroke-width="2"/></svg>
    <p class="service-name">CRM Implementations</p>
    <p class="service-text">Take your relationships to the next level</p>
  </div>
  <div class="service-card" style="left:335px;top:1988px">
    <svg class="service-icon" width="40" height="40" viewBox="0 0 40 40"><rect x="8" y="20" width="5" height="12" fill="#2b62a3"/><rect x="16" y="14" width="5" height="18" fill="#2b62a3"/><rect x="24" y="9" width="5" height="23" fill="#2b62a3"/><circle cx="30" cy="10" r="5" fill="#f7dc74"/></svg>
    <p class="service-name">BI And Data</p>
    <p class="service-text">Discover, connect, and trust your data</p>
  </div>
  <div class="service-card" style="left:609px;top:1988px">
    <svg class="service-icon" width="44" height="40" viewBox="0 0 44 40"><circle cx="14" cy="14" r="5" fill="#2b62a3"/><circle cx="30" cy="14" r="5" fill="#2b62a3"/><path d="M5 30c0-6 4-9 9-9s9 3 9 9zM21 30c0-6 4-9 9-9s9 3 9 9z" fill="#2b62a3"/><circle cx="22" cy="10" r="4" fill="#f7dc74"/></svg>
    <p class="service-name">Building The Right Team Of People</p>
    <p class="service-text">Hire resources for your transformation journey</p>
  </div>
  <p class="centered caption" style="top:2212px">Find out how Norvalith can help you put all the pieces together and get them done.</p>

  <!-- people -->
  <section class="centered" style="top:2560px">
    <p class="eyebrow">Resources</p>
    <h2 class="section-title" style="margin-top:10px">It’s The People</h2>
    <span class="title-rule" style="width:60px;margin-top:2px"></span>
    <p class="people-copy" style="width:700px;margin:20px auto 0">The world has changed in the past twenty years. The people you need might not all work for one company. Our clients want the best resources, available quickly. That’s why, in addition to our team of experts, we partner with:</p>
    <p class="small" style="margin-top:22px;line-height:2.3;font-size:9.5px">• A large network of expert consultants who are the best at what they do.<br>• Service providers all over the world to provide the resources and value that are right for you, available 24 x 7.</p>
    <p class="people-copy" style="margin-top:14px">People are invariably at the center of our customer’s success. Find out how we can add our experts to yours.</p>
  </section>
  <span class="avatar ring" style="left:260px;top:2545px;width:52px;height:52px" role="img" aria-label="Portrait of a consultant"></span>
  <span class="avatar ring" style="left:909px;top:2525px;width:104px;height:104px" role="img" aria-label="Portrait of a consultant"></span>
  <span class="avatar" style="left:1081px;top:2628px;width:32px;height:32px" role="img" aria-label="Portrait of a consultant"></span>
  <span class="avatar soft" style="left:176px;top:2652px;width:36px;height:40px" role="img" aria-label="Blurred portrait of a consultant"></span>
  <span class="avatar" style="left:96px;top:2773px;width:48px;height:48px" role="img" aria-label="Portrait of a consultant"></span>
  <span class="avatar soft" style="left:978px;top:2746px;width:72px;height:72px" role="img" aria-label="Portrait of a consultant"></span>
  <span class="avatar ring" style="left:244px;top:2852px;width:100px;height:100px" role="img" aria-label="Portrait of a consultant"></span>
  <span class="avatar ring" style="left:780px;top:2868px;width:68px;height:68px" role="img" aria-label="Portrait of a consultant"></span>

  <!-- testimonials -->
  <svg class="quote-mark" width="190" height="150" viewBox="0 0 190 150" aria-hidden="true">
    <path d="M40 10c-22 0-34 14-34 34 0 22 16 34 34 34 4 0 8-1 10-2-2 26-20 50-44 62 38-8 70-40 70-84 0-28-14-44-36-44z" fill="none" stroke="#f0c21a" stroke-width="3"/>
    <path d="M136 10c-22 0-34 14-34 34 0 22 16 34 34 34 4 0 8-1 10-2-2 26-20 50-44 62 38-8 70-40 70-84 0-28-14-44-36-44z" fill="none" stroke="#f0c21a" stroke-width="3"/>
  </svg>
  <section class="reviews">
    <p class="eyebrow">Reviews</p>
    <h2 class="reviews-title">Testimonials</h2>
    <p class="small">Lorem Ipsum is simply dummy text of the printing and typesetting industry. Lorem Ipsum has been the industry’s standard dummy text ever since the 1500s</p>
    <span class="btn btn-view">View All</span>
  </section>

  <article class="review-card" style="left:609px;top:3201px">
    <div class="review-head"><span class="review-face" role="img" aria-label="Reviewer portrait"></span><div><p class="review-name">JOHN DOE</p><p class="stars">★★★★★</p></div></div>
    <svg class="review-quote" width="46" height="30" viewBox="0 0 46 30"><path d="M4 26c8-2 14-8 14-16 0-5-3-8-7-8S4 5 4 9s3 7 7 7M26 26c8-2 14-8 14-16 0-5-3-8-7-8s-7 3-7 7 3 7 7 7" fill="none" stroke="#f0c21a" stroke-width="1.5"/></svg>
    <p class="small">when an unknown printer took a galley of type and scrambled it to make a type specimen book. It has survived not only five centuries, but also the leap into electronic typesetting, remaining essentially unchanged.</p>
  </article>
  <article class="review-card" style="left:688px;top:3418px">
    <div class="review-head"><span class="review-face" role="img" aria-label="Reviewer portrait"></span><div><p class="review-name">JOHN DOE</p><p class="stars">★★★★★</p></div></div>
    <svg class="review-quote" width="46" height="30" viewBox="0 0 46 30"><path d="M4 26c8-2 14-8 14-16 0-5-3-8-7-8S4 5 4 9s3 7 7 7M26 26c8-2 14-8 14-16 0-5-3-8-7-8s-7 3-7 7 3 7 7 7" fill="none" stroke="#f0c21a" stroke-width="1.5"/></svg>
    <p class="small">when an unknown printer took a galley of type and scrambled it to make a type specimen book. It has survived not only five centuries, but also the leap into electronic typesetting, remaining essentially unchanged.</p>
  </article>
  <span class="dot" style="left:967px;top:3266px;width:10px;height:10px;background:var(--yellow)"></span>
  <span class="dot" style="left:968px;top:3300px;width:6px;height:6px"></span>
  <span class="dot" style="left:968px;top:3334px;width:6px;height:6px"></span>

  <div class="pixel-field" style="left:880px;top:3700px;width:320px;height:220px;background:radial-gradient(ellipse at 60% 50%,rgba(43,98,163,.4),rgba(240,194,26,.25) 55%,transparent 75%)" role="img" aria-label="Scattered blue and yellow pixel squares"></div>

  <!-- technologies -->
  <section class="centered" style="top:3940px">
    <p class="eyebrow">Norvalith</p>
    <h2 class="section-title" style="margin-top:10px">Technologies</h2>
  </section>
  <span class="carousel-arrow" style="left:96px"><svg width="60" height="60" viewBox="0 0 60 60"><path d="M42 30H18M24 24l-6 6 6 6" fill="none" stroke="#2b62a3" stroke-width="1.5"/></svg></span>
  <span class="carousel-arrow" style="left:1040px"><svg width="60" height="60" viewBox="0 0 60 60"><path d="M18 30h24M36 24l6 6-6 6" fill="none" stroke="#2b62a3" stroke-width="1.5"/></svg></span>
  <article class="tech-card" style="left:197px">
    <div class="tech-photo" style="background:linear-gradient(160deg,#d7d3cc,#8b8178 55%,#3e3a36)" role="img" aria-label="Hands typing on a laptop showing an order table"></div>
    <p class="tech-label">Order Processing</p>
  </article>
  <article class="tech-card" style="left:471px">
    <div class="tech-photo" style="background:linear-gradient(160deg,#e6e8ec,#9ea6b2 55%,#4a4f58)" role="img" aria-label="Person reviewing a bar chart on a tablet"></div>
    <p class="tech-label">Sales Automation</p>
  </article>
  <article class="tech-card" style="left:747px">
    <div class="tech-photo" style="background:linear-gradient(160deg,#c7d2e0,#5d6f8a 50%,#2b2f3c 80%,#d8a63c)" role="img" aria-label="Hands on a laptop with glowing marketing icons"></div>
    <p class="tech-label">Marketing Automation</p>
  </article>

  <div class="pixel-field" style="left:860px;top:4430px;width:340px;height:240px;background:radial-gradient(ellipse at 60% 50%,rgba(43,98,163,.4),rgba(240,194,26,.25) 55%,transparent 75%)" role="img" aria-label="Scattered blue and yellow pixel squares"></div>

  <!-- footer -->
  <div class="brand footer-brand"><span class="brand-mark"></span>Norvalith</div>
  <p class="footer-about">Lorem Ipsum is simply dummy text of the printing and typesetting industry. Lorem Ipsum has been the industry’s standard dummy text ever since the 1500s</p>
  <p class="copyright">© Copyright 2023 Norvalith</p>
  <div class="socials"><span></span><span></span><span></span><span></span></div>

  <div class="footer-col" style="left:534px">
    <h4>Links</h4>
    <ul><li>Home</li><li>About Us</li><li>Services</li><li>Insights</li><li>Join Us</li></ul>
  </div>
  <div class="footer-col" style="left:664px">
    <h4>Company</h4>
    <ul><li>Community</li><li>Blog</li><li>Forums</li><li>Meetups</li></ul>
  </div>
  <div class="footer-col" style="left:816px">
    <h4>Contact</h4>
    <div style="margin-top:10px">
      <div class="contact-row"><span class="contact-icon"><svg width="14" height="14" viewBox="0 0 14 14"><path d="M3 1l2 3-1 2c1 2 2 3 4 4l2-1 3 2-1 2C6 13 1 8 1 2z" fill="#fff"/></svg></span>(612) 555-0147</div>
      <div class="contact-row"><span class="contact-icon"><svg width="14" height="12" viewBox="0 0 14 12"><rect x="1" y="1" width="12" height="10" rx="1" fill="#fff"/><path d="M1 2l6 5 6-5" fill="none" stroke="#141414" stroke-width="1"/></svg></span>info@norvalith.com</div>
      <div class="contact-row"><span class="contact-icon"><svg width="12" height="14" viewBox="0 0 12 14"><path d="M6 13S1 8 1 5a5 5 0 0110 0c0 3-5 8-5 8z" fill="#fff"/><circle cx="6" cy="5" r="1.8" fill="#141414"/></svg></span>480 Lakeview Plaza Suite<br>210, Minneapolis, MN 55402</div>
    </div>
  </div>

</div>
</body>
</html>
```